Website Design for L K Harlow Harvest Ministries
Religion and Spirituality
This ministry aims to provide
Traditional
see logo for referencing
logo ai file
logo in gif
Please use this photo on the Home Page along with the "welcome" comments.
Thanks!
Morning Bread tab

```html
<!DOCTYPE html>
<html lang="en">
<head>
<meta charset="utf-8">
<title>L K Harlow Harvest Ministries</title>
<link href="https://fonts.googleapis.com/css2?family=Arimo:ital,wght@0,400;0,700;1,400&family=Noto+Serif:ital,wght@0,400;0,700;1,400&display=swap" rel="stylesheet">
<style>
:root{
  --page:#e6e8ea;
  --paper:#ffffff;
  --navy:#0d5e9c;
  --nav-top:#1e7fc4;
  --nav-bottom:#0a5a98;
  --nav-active:#063f70;
  --orange:#f07d1a;
  --green:#5fa832;
  --green-dark:#3f8a20;
  --text:#3a3a3a;
  --muted:#555;
  --title:#1b6aa8;
  --footer:#0f64a3;
}
*{box-sizing:border-box;margin:0;padding:0}
html,body{width:1200px;height:741px;overflow:hidden}
body{background:var(--page);font-family:"Arimo",Arial,sans-serif;color:var(--text);position:relative}
.site{position:absolute;left:144px;top:0;width:912px;height:741px;background:var(--paper);box-shadow:0 0 8px rgba(0,0,0,.12)}
.site::before{content:"";position:absolute;left:0;right:0;top:0;height:4px;background:var(--orange)}
.brand{position:absolute;left:22px;top:20px;display:flex;align-items:center;gap:12px}
.brand-mark{width:22px;height:22px;border-radius:50%;background:var(--green)}
.brand-name{font-family:"Noto Serif",Georgia,serif;font-weight:700;color:var(--navy);font-size:24px;line-height:27px}
.contact{position:absolute;right:22px;top:12px;text-align:right;font-size:12px;line-height:16px}
.contact .lead{font-weight:700;color:#222}
.contact .phone{font-size:24px;line-height:30px;font-weight:700;color:var(--orange);display:flex;align-items:center;justify-content:flex-end;gap:8px}
.contact .email{font-weight:700;color:var(--green-dark)}
.nav{position:absolute;left:8px;right:8px;top:100px;height:40px;background:linear-gradient(var(--nav-top),var(--nav-bottom));display:flex}
.nav a{color:#fff;text-decoration:none;font-weight:700;font-size:14px;line-height:40px;padding:0 30px;border-right:1px solid rgba(255,255,255,.25)}
.nav a.active{background:var(--nav-active)}
.hero{position:absolute;left:8px;right:8px;top:144px;height:300px;overflow:hidden;background:radial-gradient(ellipse at 38% 45%,#ffd27a 0%,#f08a2a 22%,#b02c10 50%,#3a0906 85%)}
.hero-copy{position:absolute;left:432px;top:88px;width:420px;color:#fff}
.hero-copy h2{font-family:"Noto Serif",Georgia,serif;font-weight:400;font-size:38px;line-height:44px}
.hero-copy .sub{font-family:"Noto Serif",Georgia,serif;font-style:italic;font-size:15px;margin:2px 0 10px}
.hero-copy p{font-size:12px;line-height:16px}
.arrow{position:absolute;top:130px;width:20px;height:40px}
.arrow.prev{left:10px}.arrow.next{right:10px}
.feature{position:absolute;top:451px;height:220px}
.feature::before{content:"";position:absolute;left:0;right:0;top:0;height:3px;background:var(--orange)}
.feature .thumb{position:absolute;left:2px;top:8px;width:96px;height:82px}
.feature h3{position:absolute;left:108px;top:16px;right:0;font-family:"Noto Serif",Georgia,serif;font-weight:700;font-size:15px;line-height:19px;color:var(--title)}
.feature p{position:absolute;left:0;right:4px;top:96px;font-size:11.5px;line-height:15px;color:var(--muted)}
.more{position:absolute;right:0;top:194px;background:var(--green);color:#fff;font-size:12px;font-weight:700;padding:4px 12px;text-decoration:none}
.f1{left:12px;width:290px}.f2{left:319px;width:290px}.f3{left:624px;width:278px}
.footer{position:absolute;left:8px;right:8px;top:684px;height:36px;background:var(--footer);color:#fff;font-size:12px;display:flex;align-items:center;justify-content:center;gap:12px}
.footer a{color:#fff}
</style>
</head>
<body>
<div class="site">
  <div class="brand"><span class="brand-mark"></span><span class="brand-name">L K Harlow Harvest<br>Ministries</span></div>
  <div class="contact">
    <div class="lead">For more information contact us:</div>
    <div>418 W. Cedar Ridge Rd, Millbrook, TX 75800</div>
    <div class="phone"><svg width="26" height="20" viewBox="0 0 26 20"><path d="M2 7c0-4 22-4 22 0l-1 3h-5l-1-3h-8l-1 3H3z" fill="#222"/><rect x="6" y="11" width="14" height="8" rx="2" fill="#222"/></svg>555-214-7390</div>
    <div class="email">email: info@lkharlow-hm.net</div>
  </div>
  <nav class="nav">
    <a href="#">HOME</a><a href="#" class="active">ABOUT US</a><a href="#">CELEBRATION PREACHING</a><a href="#">MORNING BREAD</a><a href="#">RESOURCES</a><a href="#">CONTACT US</a>
  </nav>
  <section class="hero" role="img" aria-label="Silhouette of a person with raised arms before a fiery red sky">
    <svg class="arrow prev" viewBox="0 0 20 40"><path d="M16 4 4 20l12 16" stroke="#fff" stroke-width="4" fill="none"/></svg>
    <svg class="arrow next" viewBox="0 0 20 40"><path d="M4 4l12 16L4 36" stroke="#fff" stroke-width="4" fill="none"/></svg>
    <div class="hero-copy">
      <h2>Gifts of helps...</h2>
      <div class="sub">Help is so essential that God established in His Church.</div>
      <p>L K Harlow Harvest Ministries offers this Ministry of Helps to Pastors and Churches who could benefit from over 50 years of ministerial experience and expertise.</p>
    </div>
  </section>
  <article class="feature f1">
    <div class="thumb" role="img" aria-label="Portrait photo of the minister and his wife" style="background:linear-gradient(#c9b7a4,#8a6f5a)"></div>
    <h3>Welcome to L K Harlow Harvest Ministries</h3>
    <p>After almost 20 years of Evangelizing and over 30 years of Pastoring, in 2006 my wife, Marian and I, entered a ministerial transition period of our lives. This transition was long foreseen and planned for by us and Grace Valley Tabernacle, the Church we formerly Pastored.</p>
    <a class="more" href="#">Read More »</a>
  </article>
  <article class="feature f2">
    <div class="thumb" role="img" aria-label="Celebration Preaching cover artwork" style="background:linear-gradient(135deg,#f3c24a,#3f8fc4)"></div>
    <h3>Celebration Preaching</h3>
    <p>L K Harlow has been known as a revivalist at heart. His ministry has touched generations across America in revivals, camps, and conferences.</p>
    <a class="more" href="#">Read More »</a>
  </article>
  <article class="feature f3">
    <div class="thumb" role="img" aria-label="Morning Bread colorful title artwork" style="background:linear-gradient(135deg,#f6e7a0,#8cc56a)"></div>
    <h3>Morning Bread</h3>
    <p>In Pastoring we found that the issues of life cause use to know, "God has not called us to see through each other, but to see each other through."</p>
    <a class="more" href="#">Read More »</a>
  </article>
  <footer class="footer">
    <span>Copyright © 2011 - 2012 www.L K Harlow Harvest Ministries. All Rights Reserved.</span>
    <a href="#">Terms of Use</a><a href="#">Policies</a><a href="#">Why Helps</a><a href="#">Funding</a><a href="#">Contact Us</a>
  </footer>
</div>
</body>
</html>
```